Wood Logging Stationary design

We need a new company logo for our stationary. Be creative. Most company apparel and hats are Navy blue and Light gray. Logo does not necessarily have to contain those two colors. Pictures of trees, logging equipment, log trucks, and logs are acceptable but not required. I am open to any and all designs. Logo must reflect our pride and professionalism in the East Texas Timber Industry.
Updates

Target Market(s)

Timber owners and sawmills. Adults 25 years and up

Industry/Entity Type

Industry

Font styles to use
Serif
Decorative

Requirements
Must have
• R. J. Pell Hauling Co.
Nice to have
• Phone number: 936-402-5817
address:
PO Box 4830
Dunmore Flats, TX 77912
www.rjpellhauling.example
rjpellhauling@mailbox.example

```html
<!DOCTYPE html>
<html lang="en">
<head>
<meta charset="utf-8">
<title>R. J. Pell Hauling Co. — Stationery</title>
<link href="https://fonts.googleapis.com/css2?family=Didact+Gothic&display=swap" rel="stylesheet">
<style>
  :root {
    --navy: #17206e;
    --paper: #ffffff;
    --backdrop: #d9d9d9;
    --shadow: rgba(0,0,0,.18);
  }
  * { box-sizing: border-box; margin: 0; padding: 0; }
  html, body { width: 1200px; height: 1080px; overflow: hidden; }
  body { background: var(--backdrop); position: relative; font-family: "Didact Gothic", sans-serif; color: var(--navy); }

  .brand-header { position: absolute; left: 0; top: 0; width: 1200px; height: 260px; background: var(--paper); display: flex; align-items: center; justify-content: center; }

  .company-name { display: flex; align-items: center; gap: .4em; font-family: "Didact Gothic", sans-serif; font-weight: 400; color: var(--navy); white-space: nowrap; }
  .company-name__square { width: .6em; height: .6em; background: var(--navy); flex: none; }
  .company-name--lg { font-size: 38px; }
  .company-name--md { font-size: 20px; }
  .company-name--sm { font-size: 12px; }

  .sheet { position: absolute; background: var(--paper); box-shadow: 0 2px 8px var(--shadow); }

  .letterhead { left: 40px; top: 295px; width: 560px; height: 725px; }
  .letterhead .company-name { position: absolute; left: 50%; top: 48px; transform: translateX(-50%); }
  .letterhead__address { position: absolute; left: 36px; bottom: 30px; font-size: 10px; line-height: 1.4; font-style: normal; }
  .letterhead__address .gap { margin-top: 10px; }
  .letterhead__web { position: absolute; right: 36px; bottom: 44px; font-size: 10px; }

  .card { width: 265px; height: 152px; top: 295px; }
  .card--front { left: 625px; display: flex; align-items: center; justify-content: center; }
  .card--back { left: 905px; background: var(--navy); color: var(--paper); padding: 16px 16px; }
  .card__name { font-size: 11px; text-align: right; }
  .card__details { margin-top: 18px; text-align: right; font-size: 9px; line-height: 1.45; font-style: normal; }
  .card__details .gap { margin-top: 7px; }
  .card__web { font-size: 10px; margin-top: 6px; }

  .envelope { left: 625px; width: 545px; height: 235px; }
  .envelope--front { top: 475px; display: flex; justify-content: center; padding-top: 44px; }
  .envelope--back { top: 735px; overflow: hidden; }
  .envelope__flap { position: absolute; left: 0; top: 0; width: 545px; height: 110px; }
  .envelope__flap-name { position: absolute; left: 0; right: 0; top: 34px; text-align: center; font-size: 17px; color: var(--paper); }
  .envelope__return { position: absolute; right: 150px; bottom: 26px; text-align: center; font-size: 9px; line-height: 1.4; font-style: normal; }
</style>
</head>
<body>

<header class="brand-header">
  <div class="company-name company-name--lg"><span class="company-name__square"></span>R. J. Pell Hauling Co.</div>
</header>

<section class="sheet letterhead" aria-label="Letterhead">
  <div class="company-name company-name--md"><span class="company-name__square"></span>R. J. Pell Hauling Co.</div>
  <address class="letterhead__address">
    <div>PO Box 4830</div>
    <div>Dunmore Flats, TX 77912</div>
    <div class="gap">Phone : 936-402-5817</div>
    <div>email : rjpellhauling@mailbox.example</div>
  </address>
  <div class="letterhead__web">www.rjpellhauling.example</div>
</section>

<section class="sheet card card--front" aria-label="Business card front">
  <div class="company-name company-name--sm"><span class="company-name__square"></span>R. J. Pell Hauling Co.</div>
</section>

<section class="sheet card card--back" aria-label="Business card back">
  <div class="card__name">R. J. Pell Hauling Co.</div>
  <address class="card__details">
    <div>PO Box 4830</div>
    <div>Dunmore Flats, TX 77912</div>
    <div class="gap">Phone : 936-402-5817</div>
    <div>email : rjpellhauling@mailbox.example</div>
    <div class="card__web">www.rjpellhauling.example</div>
  </address>
</section>

<section class="sheet envelope envelope--front" aria-label="Envelope front">
  <div class="company-name company-name--md"><span class="company-name__square"></span>R. J. Pell Hauling Co.</div>
</section>

<section class="sheet envelope envelope--back" aria-label="Envelope back">
  <svg class="envelope__flap" viewBox="0 0 545 110" preserveAspectRatio="none" aria-hidden="true">
    <path d="M0 0 H545 V20 C430 60 300 110 170 100 C90 95 40 85 0 95 Z" fill="var(--navy)"/>
  </svg>
  <div class="envelope__flap-name">R. J. Pell Hauling Co.</div>
  <address class="envelope__return">
    <div>PO Box 4830</div>
    <div>Dunmore Flats, TX 77912</div>
    <div>Phone : 936-402-5817</div>
    <div>email : rjpellhauling@mailbox.example</div>
    <div>www.rjpellhauling.example</div>
  </address>
</section>

</body>
</html>
```